Retail Appliance Store Chain needs NEW business Card

Name of my company is Brandon's Appliances brandonsappliances.com is our website. . We are a 2 location brick and mortar, and online store selling premium, luxury, and normal household appliances, such as ovens, stoves, cooktops, dishwashers, refrigerators, washers and dryers, grills, air conditioners etc. The focus is on large kitchen appliances and laundry appliances.
Please visit http://brandonsappliances.com to get a feel for the business and branding.
I have attached the Brandon's Appliances logo (i do not have eps or psd or ai). And I have also attached our current business cards that we use. We have two versions. A double sided version for managers, and a one side version for regular employees.
Please submit BOTH one sided and two sided designs if possible.
Please keep consistent with the Brandon's Appliances logo, colors, etc.
I would prefer no rounded corners on the business card designs for printing costs.
Information on the cards (in no particular order):
Name - Employee Name
Business name - Brandon's Appliances
website - brandonsappliances.com
Email - Employee Email
2 Phone Numbers - store 1 address, store 2 address
2 Addresses - store 1 address, store 2 address

*do NOT need Fax #

Industry/Entity Type

Home Appliance

Contact Information for Business Card

Logo - Brandons Appliances Logo
Name - Employee Name
Email - Employee Email

Please no rounded corners. Standard US Business Card Size please.

Font styles to use
Serif
Sans Serif

Requirements
Must have
• colors and design that somewhat match the feel of current logo and website
Should not have
• No rounded corners.
No non-traditional business card size. US Standard Business Card Size only

```html
<!DOCTYPE html>
<html lang="en">
<head>
<meta charset="utf-8">
<title>Brandon's Appliances – Business Card</title>
<link href="https://fonts.googleapis.com/css2?family=Arimo:wght@400;700&display=swap" rel="stylesheet">
<style>
  :root {
    --stage: #1d1e21;
    --paper: #ffffff;
    --brand: #1f6fb8;
    --brand-deep: #0b3f8f;
    --brand-mid: #1456b0;
    --ink-grey: #8a8d91;
    --band: #2a78bf;
  }
  * { margin: 0; padding: 0; box-sizing: border-box; }
  html, body { width: 1200px; height: 900px; overflow: hidden; }
  body {
    background: var(--stage);
    font-family: "Arimo", Arial, sans-serif;
    position: relative;
  }
  .card {
    position: absolute;
    left: 250px;
    width: 700px;
    height: 400px;
    overflow: hidden;
  }
  .card-front { top: 35px; background: var(--paper); }
  .card-back {
    top: 465px;
    background: radial-gradient(ellipse at 45% 40%, var(--brand-mid) 0%, var(--brand-deep) 100%);
    color: #fff;
  }

  /* front */
  .front-band {
    position: absolute; left: 0; bottom: 0; width: 100%; height: 22px;
    background: var(--band);
  }
  .holder { position: absolute; left: 48px; top: 48px; }
  .holder-name {
    font-weight: 700; font-size: 24px; color: var(--brand);
    letter-spacing: 0.5px; text-transform: uppercase;
  }
  .holder-role, .holder-branch {
    font-weight: 700; font-size: 14px; color: var(--ink-grey); margin-top: 3px;
  }
  .brand-block { position: absolute; right: 48px; top: 160px; text-align: right; }
  .brand-name {
    font-weight: 700; font-size: 32px; color: var(--brand); white-space: nowrap;
  }
  .divider {
    position: absolute; left: 300px; right: 48px; top: 232px;
    height: 2px; background: var(--brand);
  }
  .contact-list { position: absolute; list-style: none; }
  .contact-list.store-one { left: 48px; top: 158px; }
  .contact-list.store-two { left: 300px; top: 256px; }
  .contact-list li {
    display: flex; align-items: flex-start; gap: 9px;
    font-weight: 700; font-size: 15px; color: var(--brand);
    line-height: 19px; margin-bottom: 6px;
  }
  .contact-icon { flex: 0 0 18px; width: 18px; height: 18px; margin-top: 1px; }

  /* back */
  .back-brand {
    position: absolute; left: 0; right: 0; top: 150px; text-align: center;
  }
  .back-brand .brand-name { color: #fff; font-size: 48px; }
  .back-web {
    position: absolute; left: 0; right: 0; bottom: 60px; text-align: center;
    font-weight: 700; font-size: 17px; color: rgba(255,255,255,0.85); letter-spacing: 0.5px;
  }
</style>
</head>
<body>

<section class="card card-front">
  <div class="holder">
    <div class="holder-name">Evan Hollis</div>
    <div class="holder-role">Bargain Basement Supervisor</div>
    <div class="holder-branch">Ashford</div>
  </div>

  <ul class="contact-list store-one">
    <li>
      <svg class="contact-icon" viewBox="0 0 18 18" aria-hidden="true"><circle cx="9" cy="9" r="8" fill="none" stroke="#1f6fb8" stroke-width="1.4"/><circle cx="9" cy="9" r="3.5" fill="none" stroke="#1f6fb8" stroke-width="1.2"/><path d="M5.5 9h7M9 5.5v7" stroke="#1f6fb8" stroke-width="1"/></svg>
      <span>brandonsappliances.com</span>
    </li>
    <li>
      <svg class="contact-icon" viewBox="0 0 18 18" aria-hidden="true"><circle cx="9" cy="9" r="8" fill="none" stroke="#1f6fb8" stroke-width="1.4"/><path d="M9 14s-3.5-3.6-3.5-6a3.5 3.5 0 0 1 7 0c0 2.4-3.5 6-3.5 6z" fill="#1f6fb8"/><circle cx="9" cy="8" r="1.2" fill="#fff"/></svg>
      <span>418 Harbor View Rd.<br>Ashford, CT 06278</span>
    </li>
    <li>
      <svg class="contact-icon" viewBox="0 0 18 18" aria-hidden="true"><circle cx="9" cy="9" r="8" fill="none" stroke="#1f6fb8" stroke-width="1.4"/><path d="M6 5l1.8-.3 1 2.2-1.1.9a6 6 0 0 0 2.5 2.5l.9-1.1 2.2 1-.3 1.8c-3.8.4-7.4-3.2-7-7z" fill="#1f6fb8"/></svg>
      <span>(555) 214-3087</span>
    </li>
  </ul>

  <div class="brand-block">
    <div class="brand-name">Brandon's Appliances</div>
  </div>

  <div class="divider"></div>

  <ul class="contact-list store-two">
    <li>
      <svg class="contact-icon" viewBox="0 0 18 18" aria-hidden="true"><circle cx="9" cy="9" r="8" fill="none" stroke="#1f6fb8" stroke-width="1.4"/><rect x="4.8" y="6" width="8.4" height="6" fill="none" stroke="#1f6fb8" stroke-width="1.1"/><path d="M4.8 6L9 9.4 13.2 6" fill="none" stroke="#1f6fb8" stroke-width="1.1"/></svg>
      <span>evanh@brandonsappliances.com</span>
    </li>
    <li>
      <svg class="contact-icon" viewBox="0 0 18 18" aria-hidden="true"><circle cx="9" cy="9" r="8" fill="none" stroke="#1f6fb8" stroke-width="1.4"/><path d="M9 14s-3.5-3.6-3.5-6a3.5 3.5 0 0 1 7 0c0 2.4-3.5 6-3.5 6z" fill="#1f6fb8"/><circle cx="9" cy="8" r="1.2" fill="#fff"/></svg>
      <span>7 Millbrook Ave.<br>Lakeview, CT 06390</span>
    </li>
    <li>
      <svg class="contact-icon" viewBox="0 0 18 18" aria-hidden="true"><circle cx="9" cy="9" r="8" fill="none" stroke="#1f6fb8" stroke-width="1.4"/><path d="M6 5l1.8-.3 1 2.2-1.1.9a6 6 0 0 0 2.5 2.5l.9-1.1 2.2 1-.3 1.8c-3.8.4-7.4-3.2-7-7z" fill="#1f6fb8"/></svg>
      <span>(555) 362-7140</span>
    </li>
  </ul>

  <div class="front-band"></div>
</section>

<section class="card card-back">
  <div class="back-brand">
    <div class="brand-name">Brandon's Appliances</div>
  </div>
  <div class="back-web">www.brandonsappliances.com</div>
</section>

</body>
</html>
```